Business card design for global fintech startup

Verdell is a modern payments platform for the global insurance industry, serving international health, life, and travel insurers, MGAs, brokers, and partners.

We need a professional, premium business card for use at insurance conferences and executive meetings. The goal is to create a card that feels trustworthy, modern, and high-quality, while still being distinctive and memorable in a stack of business cards.

Target audience:
Senior insurance executives (VP, C-suite).

Design goals:
Clear, professional, and credible
Modern but not trendy
Premium and well-structured
Easy to read and practical for networking

Brand direction:
Brand-first (company over individual)
Follow existing brand guidelines where possible
Clean layout, strong hierarchy, excellent readability

Must include:
Name
Title
Company name (Verdell)
Logo
Email
Phone/Whatsapp
Website (www.joinverdell.com)
Tagline - Trust that moves money

Materials & finish:
Open to designer recommendations for premium look and feel.

Please avoid:
Flashy or trendy startup styles
Generic insurance icons or clichés
Cluttered layouts or hard-to-read text

Deliverables:
Front and back business card, print-ready files.

Target Market(s)

Global Insurance executives

Industry/Entity Type

Fintech, Insurtech, Insurance, Financial Services

Contact Information for Business Card

Name Title Company name (Verdell) Logo Email Phone/Whatsapp Website (www.joinverdell.com) Tagline - Trust that moves money

Font styles to use
Other font styles liked:
• See brand guidelines

Requirements
Nice to have
• something that stands out/makes us more memorable while still remaining professional
Should not have
• Please avoid: Flashy or trendy startup styles Generic insurance icons or clichés Cluttered layouts or hard-to-read text

```html
<!DOCTYPE html>
<html lang="en">
<head>
<meta charset="UTF-8">
<title>Verdell business card, back and front</title>
<link rel="stylesheet" href="https://fonts.googleapis.com/css2?family=Poppins:wght@400;500;600&display=swap">
<style>
  :root {
    --stage: #2b2b2b;
    --card-dark: #1c1c1c;
    --card-light: #ffffff;
    --ink-dark: #151515;
    --ink-light: #ffffff;
    --icon-blue: #2f7fd0;
  }
  * { margin: 0; padding: 0; box-sizing: border-box; }
  html, body { width: 1200px; height: 875px; overflow: hidden; }
  body {
    background: var(--stage);
    font-family: "Poppins", sans-serif;
    position: relative;
  }
  .card {
    position: absolute;
    top: 287px;
    width: 520px;
    height: 300px;
    border-radius: 22px;
    box-shadow: 0 18px 40px rgba(0,0,0,0.45);
  }
  .card-back {
    left: 50px;
    background: var(--card-dark);
    color: var(--ink-light);
  }
  .card-front {
    left: 630px;
    background: var(--card-light);
    color: var(--ink-dark);
  }
  .wordmark {
    font-weight: 500;
    letter-spacing: 0.14em;
    line-height: 1;
    display: flex;
    align-items: center;
    gap: 16px;
  }
  .wordmark-dot {
    width: 14px;
    height: 14px;
    border-radius: 50%;
    background: currentColor;
    flex: none;
  }
  .card-back .wordmark {
    position: absolute;
    left: 0; right: 0;
    top: 112px;
    justify-content: center;
    font-size: 50px;
  }
  .tagline {
    position: absolute;
    left: 0; right: 0;
    top: 190px;
    text-align: center;
    font-size: 13px;
    letter-spacing: 0.03em;
  }
  .card-front .wordmark {
    position: absolute;
    left: 42px;
    top: 44px;
    font-size: 40px;
  }
  .person {
    position: absolute;
    left: 42px;
    top: 116px;
  }
  .person-name { font-size: 19px; font-weight: 600; line-height: 1.2; }
  .person-title { font-size: 11px; line-height: 1.4; }
  .address {
    position: absolute;
    left: 42px;
    top: 172px;
    font-size: 11px;
    line-height: 1.45;
  }
  .contacts {
    position: absolute;
    left: 42px;
    top: 222px;
    list-style: none;
    font-size: 11px;
    line-height: 1.5;
  }
  .contacts li { display: flex; align-items: center; gap: 8px; }
  .contacts svg { width: 10px; height: 10px; fill: var(--icon-blue); flex: none; }
</style>
</head>
<body>
  <section class="card card-back" aria-label="Card back">
    <div class="wordmark"><span class="wordmark-dot"></span>VERDELL</div>
    <p class="tagline">Trust that moves money</p>
  </section>

  <section class="card card-front" aria-label="Card front">
    <div class="wordmark"><span class="wordmark-dot"></span>VERDELL</div>
    <div class="person">
      <p class="person-name">Daniel Hart</p>
      <p class="person-title">CEO &amp; Founder</p>
    </div>
    <p class="address">1408 Harbor Ln.<br>Bayview FL 32501</p>
    <ul class="contacts">
      <li>
        <svg viewBox="0 0 10 10" aria-hidden="true"><path d="M2 0.5 L3.8 0.5 L4.4 2.8 L3.2 3.8 Q4.2 5.8 6.2 6.8 L7.2 5.6 L9.5 6.2 L9.5 8 Q9.5 9.5 8 9.5 Q0.5 9 0.5 2 Q0.5 0.5 2 0.5Z"/></svg>
        555-014-2290
      </li>
      <li>
        <svg viewBox="0 0 10 10" aria-hidden="true"><path d="M0.5 2 L9.5 2 L9.5 8 L0.5 8Z M1 2.5 L5 5.5 L9 2.5" stroke="#fff" stroke-width="0.8"/></svg>
        daniel@joinverdell.com
      </li>
      <li>
        <svg viewBox="0 0 10 10" aria-hidden="true"><circle cx="5" cy="5" r="4.5"/><path d="M0.5 5 H9.5 M5 0.5 Q2.5 5 5 9.5 Q7.5 5 5 0.5" stroke="#fff" stroke-width="0.6" fill="none"/></svg>
        www.joinverdell.com
      </li>
    </ul>
  </section>
</body>
</html>
```